Floorplan brochure design for rental company

We need a brochure designed for our rental company, Bramble Tor Commons.
We have two different categories that we need on this brochure: townhomes (primary) and mobile homes. Size and layout is up to you... choose what you think works best for the information being presented. However, please do not use an odd shape or size; do use a size and format that can be printed by qelvaprint.com.
Font and color choices are up to you. If needed, the fonts from the logo are Americana Extra Bold and BlackJack.
Industry/Entity Type
It Company
Requirements
Must have
- 1. logo and office address/contact information
2. floorplans and prices from attached documents
3. amenities from attached document
Should not have
- Please do not use our website, brambletor.com, as a basis for any design or color scheme decisions. We are working on a redesign of that website with our new logo (attached).

```html
<!DOCTYPE html>
<html lang="en">
<head>
<meta charset="utf-8">
<title>Bramble Tor Commons – Townhomes &amp; Mobile homes brochure</title>
<link rel="stylesheet" href="https://fonts.googleapis.com/css2?family=Roboto:wght@400;500;700;900&family=Roboto+Condensed:wght@400;700&display=swap">
<style>
  :root {
    --paper: #ffffff;
    --canvas: #ffffff;
    --edge: #c9c9c9;
    --mint: #d5e6d1;
    --sky: #c9e7f3;
    --leaf: #3c9b3f;
    --ocean: #1b9ad7;
    --ink: #222222;
    --grey: #6f6f6f;
    --grey-soft: #8a8a8a;
    --rule: #cfcfcf;
    --plan-fill: #eeeeee;
    --plan-line: #9a9a9a;
  }
  * { box-sizing: border-box; margin: 0; padding: 0; }
  html, body { width: 1200px; height: 1200px; overflow: hidden; background: var(--canvas); }
  body { position: relative; font-family: "Roboto", Arial, sans-serif; color: var(--ink); }

  .page {
    position: absolute; top: 235px; width: 529px; height: 682px;
    background: var(--paper); border: 1px solid var(--edge); overflow: hidden;
  }
  .page--cover { left: 54px; }
  .page--plans { left: 622px; }

  .cover-bands { position: absolute; inset: 0; }

  /* Cover brand */
  .brand { position: absolute; left: 40px; top: 62px; width: 170px; text-align: center; }
  .brand__dot { width: 64px; height: 64px; border-radius: 50%; background: var(--leaf); margin: 0 auto 14px; }
  .brand__name { font-weight: 700; color: var(--leaf); font-size: 23px; line-height: 1.08; }

  .cover-title { position: absolute; left: 280px; top: 118px; width: 220px; text-align: center;
    font-weight: 700; font-size: 24px; line-height: 1.1; letter-spacing: -0.2px; }
  .cover-title .t-town { color: var(--leaf); display: block; }
  .cover-title .t-mobile { color: var(--ocean); display: block; }

  .amenities { position: absolute; left: 114px; top: 253px; width: 340px; color: var(--grey); }
  .amenities__title { font-family: "Roboto Condensed", Arial, sans-serif; font-weight: 700; font-size: 16px; color: #666; margin-bottom: 3px; }
  .amenities__cols { display: flex; gap: 0; }
  .amenities__col { width: 170px; }
  .amenities__col--right { margin-top: -20px; }
  .amenities h4 { font-family: "Roboto Condensed", Arial, sans-serif; font-weight: 700; font-size: 11.5px; color: #666; line-height: 15.4px; }
  .amenities ul { list-style: none; font-family: "Roboto Condensed", Arial, sans-serif; font-size: 11.5px; line-height: 15.4px; }
  .amenities li::before { content: "• "; }
  .amenities li.wrap { padding-left: 8px; text-indent: -8px; }
  .amenities .group-gap { margin-top: 15px; }
  .amenities__note { font-size: 8px; margin-top: 6px; color: var(--grey-soft); }

  .contact { position: absolute; right: 74px; top: 561px; text-align: right;
    font-family: "Roboto Condensed", Arial, sans-serif; color: var(--ink); }
  .contact__title { font-weight: 700; font-size: 15.5px; margin-bottom: 5px; }
  .contact p { font-size: 12.5px; line-height: 17px; }
  .contact strong { font-weight: 700; }

  /* Plans page */
  .section-title { position: absolute; left: 28px; font-weight: 700; font-size: 19px; letter-spacing: -0.2px; }
  .section-title--town { top: 29px; color: var(--leaf); }
  .section-title--mobile { top: 270px; color: var(--ocean); }

  .plan { position: absolute; background: var(--plan-fill); border: 1px solid var(--plan-line); }
  .plan-num { position: absolute; font-weight: 700; font-size: 10px; color: var(--ink); }

  .price-list { position: absolute; left: 30px; font-family: "Roboto Condensed", Arial, sans-serif; font-size: 10px; color: var(--ink); border-collapse: collapse; }
  .price-list td { padding: 0; height: 14.5px; vertical-align: middle; white-space: nowrap; }
  .price-list .plan-name, .price-list .plan-price { font-weight: 700; font-size: 11px; }
  .price-list--town { top: 181px; }
  .price-list--town .plan-name, .price-list--town .plan-price { color: var(--leaf); }
  .price-list--mobile { top: 558px; }
  .price-list--mobile .plan-name, .price-list--mobile .plan-price { color: var(--ocean); }
  .price-list .c-name { width: 64px; }
  .price-list .c-price { width: 44px; }

  .divider { position: absolute; left: 28px; top: 258px; width: 475px; height: 1px; background: var(--rule); }

  .corner-brand { position: absolute; left: 408px; top: 582px; width: 110px; text-align: center; }
  .corner-brand__dot { width: 34px; height: 34px; border-radius: 50%; background: var(--leaf); margin: 0 auto 6px; }
  .corner-brand__name { font-weight: 700; color: var(--leaf); font-size: 13px; line-height: 1.1; }
</style>
</head>
<body>

<section class="page page--cover">
  <svg class="cover-bands" width="529" height="682" viewBox="0 0 529 682" aria-hidden="true">
    <path d="M0 0 H529 V176 C420 205 250 215 150 225 C90 231 40 236 0 240 Z" fill="var(--mint)"/>
    <path d="M0 596 C120 566 300 540 529 532 V682 H0 Z" fill="var(--sky)"/>
  </svg>

  <div class="brand">
    <div class="brand__dot"></div>
    <div class="brand__name">Bramble Tor<br>Commons</div>
  </div>

  <h1 class="cover-title"><span class="t-town">Townhomes</span><span class="t-mobile">Mobile homes</span></h1>

  <div class="amenities">
    <h2 class="amenities__title">Amenities</h2>
    <div class="amenities__cols">
      <div class="amenities__col">
        <h4>Overall features:</h4>
        <ul>
          <li>Golf course</li>
          <li>Convenience store</li>
          <li>Gated access</li>
          <li>Playground</li>
          <li>Basketball courts</li>
          <li>Stocked fishing lake</li>
          <li>Pet friendly*</li>
          <li>Dog park</li>
          <li>Extra storage available</li>
          <li>Lawn care included</li>
          <li>Outdoor grills permitted</li>
        </ul>
        <p class="amenities__note">*breed restrictions</p>
      </div>
      <div class="amenities__col amenities__col--right">
        <h4 style="margin-top:20px">Townhomes:</h4>
        <ul>
          <li>6 Foot privacy fenced backyard</li>
          <li>Concrete backyard patio</li>
          <li>Assigned front door parking</li>
          <li>Ceiling fans in every room</li>
          <li class="wrap">Dishwasher, microwave, refrigerator and range</li>
          <li class="wrap">Full size washer and dryer connections</li>
        </ul>
        <h4 class="group-gap">Mobile homes:</h4>
        <ul>
          <li>Large fenced backyards</li>
          <li>Concrete patio</li>
          <li>Private driveway</li>
        </ul>
      </div>
    </div>
  </div>

  <div class="contact">
    <h3 class="contact__title">For more information</h3>
    <p>Call <strong>281-555-0172</strong></p>
    <p>Visit <strong>www.brambletor.com</strong></p>
    <p>Or call by our office at <strong>1870 Wren Hollow Rd, Alder Bend, TX, 77406</strong></p>
  </div>
</section>

<section class="page page--plans">
  <h2 class="section-title section-title--town">Townhomes</h2>

  <span class="plan-num" style="left:20px;top:60px">1</span>
  <div class="plan" style="left:28px;top:62px;width:172px;height:111px" role="img" aria-label="Floor plan 1: two-storey townhome with two bedrooms upstairs, kitchen, dining and living room downstairs"></div>
  <span class="plan-num" style="left:206px;top:60px">2</span>
  <div class="plan" style="left:213px;top:62px;width:158px;height:111px" role="img" aria-label="Floor plan 2: two-storey townhome with two bedrooms upstairs, kitchen, dining and living room downstairs"></div>
  <span class="plan-num" style="left:376px;top:60px">3</span>
  <div class="plan" style="left:384px;top:62px;width:119px;height:149px" role="img" aria-label="Floor plan 3: single-level townhome with master suite, second bedroom, kitchen, dining and living room"></div>

  <table class="price-list price-list--town">
    <tr><td class="c-name plan-name">1.&nbsp; Plan 1132</td><td class="c-price plan-price">$875</td><td>2 br, 2.5 bath, 2 storey</td></tr>
    <tr><td class="c-name plan-name">2.&nbsp; Plan 1272</td><td class="c-price plan-price">$925</td><td>2 br, 2.5 bath, 2 storey</td></tr>
    <tr><td class="c-name plan-name">3.&nbsp; Plan 1069</td><td class="c-price plan-price">$900</td><td>2 br, 2 bath</td></tr>
    <tr><td class="c-name plan-name">&nbsp;&nbsp;&nbsp;&nbsp; Plan 1070</td><td class="c-price plan-price">$925</td><td>2 br, 2 bath, covered patio</td></tr>
  </table>

  <div class="divider"></div>

  <h2 class="section-title section-title--mobile">Mobile homes</h2>

  <span class="plan-num" style="left:20px;top:305px">4</span>
  <div class="plan" style="left:28px;top:308px;width:297px;height:71px" role="img" aria-label="Floor plan 4: 16 by 76 mobile home with three bedrooms, two baths, kitchen, dining and living room"></div>
  <span class="plan-num" style="left:20px;top:389px">5</span>
  <div class="plan" style="left:28px;top:392px;width:297px;height:71px" role="img" aria-label="Floor plan 5: 16 by 76 mobile home with three bedrooms, two baths, kitchen and living room"></div>
  <span class="plan-num" style="left:20px;top:473px">6</span>
  <div class="plan" style="left:28px;top:476px;width:222px;height:72px" role="img" aria-label="Floor plan 6: 16 by 52 mobile home with two bedrooms, one bath, kitchen and living room"></div>
  <span class="plan-num" style="left:270px;top:475px">7</span>
  <div class="plan" style="left:281px;top:478px;width:222px;height:72px;border:2px solid #333" role="img" aria-label="Floor plan 7: 11 by 35 mobile home with one bedroom, one bath, kitchen, dining and living room"></div>

  <table class="price-list price-list--mobile">
    <tr><td class="c-name plan-name">4.&nbsp; Plan 1887</td><td class="c-price plan-price">$875</td><td>16' x 76' 3br, 2 bath</td></tr>
    <tr><td class="c-name"></td><td class="c-price plan-price">$950</td><td>16' x 76' 3br, 2 bath, with 8' x 8' storage bldg</td></tr>
    <tr><td class="c-name plan-name">5.&nbsp; Plan 2762</td><td class="c-price plan-price">$850</td><td>16' x 76' 3br, 2 bath</td></tr>
    <tr><td class="c-name plan-name">6.&nbsp; Plan 1648</td><td class="c-price plan-price">$750</td><td>16' x 52' 2br, 1 bath</td></tr>
    <tr><td class="c-name plan-name">7.&nbsp; Plan 105</td><td class="c-price plan-price">$1050</td><td>11' x 35' 1br, 1 bath, furnished including utilities</td></tr>
  </table>

  <div class="corner-brand">
    <div class="corner-brand__dot"></div>
    <div class="corner-brand__name">Bramble Tor<br>Commons</div>
  </div>
</section>

</body>
</html>
```